Construction company focused on concrete and shed construction.

We need to update our current business card for ridgeforgebuilds.com.au we would like an eye catching design with blue, grey and white incorporating our current logo.
Our company started off in concreting and due to varying factors we have expanded to include shed construction as well.
This has led to our current Logo looking a little out of place and somehow need to use the card to bring in the shed construction side of the business while not having to change current concrete look "KESTRO" logo as we already have this incorporated into our company clothing and are not willing to change this yet.
Photo image attached for inspiration/ visual reference of type of work, not to be used on final design.
Please no cheesy designs of men in hard hats and tools
Final design should demonstrate a modern and service focused company.

Target Market(s)

Farmers, Business owners, Developers, Architects, Commercial project delivery

Industry/Entity Type

Construction Company

Contact Information for Business Card

Kestro Constructions.
7b Harlow st
East Kelvale Tas
03 62918873

Font styles to use
Other font styles liked:
• see font in logo

Colors
3176b5
b2b2b2

Requirements
Must have
• Easy to read font,
• good contrast between back ground and writing
Nice to have
• Modern and corporate look with a fun but professional image.
Should not have
• Comic images or shadow images of tools/ people.

```html
<!DOCTYPE html>
<html lang="en">
<head>
<meta charset="utf-8">
<title>Kestro Constructions – Business Card</title>
<link href="https://fonts.googleapis.com/css2?family=Lato:wght@400;700&display=swap" rel="stylesheet">
<style>
  :root {
    --backdrop: #1d1d1d;
    --brand-blue: #1a5f9c;
    --brand-blue-light: #3176b5;
    --slate: #4a545a;
    --paper: #e4e8ec;
    --white: #ffffff;
    --marble-a: #55606a;
    --marble-b: #7d878f;
    --marble-c: #3c4850;
  }
  * { box-sizing: border-box; margin: 0; padding: 0; }
  html, body {
    width: 1200px; height: 900px; overflow: hidden;
    background: var(--backdrop);
    font-family: "Lato", Arial, sans-serif;
  }
  .stage { position: relative; width: 1200px; height: 900px; }
  .card {
    position: absolute; top: 306px;
    width: 439px; height: 271px;
    border-radius: 10px; overflow: hidden;
    box-shadow: 0 4px 10px rgba(0,0,0,.45);
  }
  .card--front { left: 149px; background: var(--paper); }
  .card--back { left: 609px; }
  .card__shapes { position: absolute; inset: 0; width: 100%; height: 100%; }
  .contact { position: absolute; color: var(--white); }
  .contact--person { left: 23px; top: 36px; }
  .person__name { font-size: 16.5px; font-weight: 400; letter-spacing: .3px; line-height: 19px; }
  .person__role { font-size: 13px; line-height: 16px; margin-top: 0; }
  .person__phone { display: flex; align-items: center; gap: 5px; font-size: 14px; line-height: 18px; margin-top: 13px; }
  .phone-icon { width: 18px; height: 18px; }
  .contact--company { left: 23px; top: 191px; font-size: 13px; line-height: 16px; }
  .company__name { font-size: 14px; font-weight: 400; letter-spacing: .2px; line-height: 17px; }
  .brand-mark {
    position: absolute; display: flex; align-items: center; justify-content: center;
    border-radius: 50%;
    font-family: "Lato", Arial, sans-serif; font-weight: 700;
    color: var(--brand-blue);
  }
  .card--front .brand-mark {
    left: 267px; top: 70px; width: 136px; height: 136px;
    border: 3px solid var(--brand-blue-light); font-size: 26px; letter-spacing: 1px;
  }
  .back__marble {
    position: absolute; inset: 0;
    background:
      radial-gradient(ellipse at 20% 30%, var(--marble-b) 0%, transparent 45%),
      radial-gradient(ellipse at 80% 75%, var(--marble-b) 0%, transparent 40%),
      linear-gradient(135deg, var(--marble-a), var(--marble-c));
  }
  .card--back .brand-mark {
    left: 150px; top: 66px; width: 139px; height: 139px;
    background: var(--paper); font-size: 26px; letter-spacing: 1px;
  }
</style>
</head>
<body>
<main class="stage">
  <section class="card card--front" aria-label="Business card front">
    <svg class="card__shapes" viewBox="0 0 439 271" preserveAspectRatio="none" aria-hidden="true">
      <path fill="var(--brand-blue)" d="M0,0 H289 C262,62 256,122 232,134 C180,136 70,136 0,138 Z"/>
      <path fill="var(--slate)" d="M0,142 C70,142 180,139 232,139 C262,150 268,218 288,271 H0 Z"/>
    </svg>
    <div class="contact contact--person">
      <p class="person__name">MARCUS HALE</p>
      <p class="person__role">Managing Director</p>
      <p class="person__phone">
        <svg class="phone-icon" viewBox="0 0 18 18" aria-hidden="true">
          <circle cx="9" cy="9" r="9" fill="var(--white)"/>
          <path fill="var(--brand-blue)" d="M6.2 4.3c.4-.2.8 0 1 .4l.8 1.7c.2.4.1.8-.2 1l-.7.6c.5 1.1 1.3 2 2.4 2.6l.6-.7c.3-.3.7-.4 1-.2l1.7.8c.4.2.6.6.4 1l-.4 1c-.2.5-.8.8-1.3.7C8.5 12.6 5.4 9.5 4.9 6.5c-.1-.5.2-1.1.7-1.3z"/>
        </svg>
        <span>03 62918873</span>
      </p>
    </div>
    <div class="contact contact--company">
      <p class="company__name">KESTRO CONSTRUCTIONS</p>
      <p>7b Harlow st</p>
      <p>East Kelvale Tas</p>
    </div>
    <div class="brand-mark">KESTRO</div>
  </section>

  <section class="card card--back" aria-label="Business card back">
    <div class="back__marble" role="img" aria-label="Flowing grey and blue marbled texture"></div>
    <div class="brand-mark">KESTRO</div>
  </section>
</main>
</body>
</html>
```